Pharmacist turned chef in Key West Fl needs a logo design

I am looking for a professional looking business card that says who I am and what I do. For example Chef Dale Morvik, natural organic and health supportive cooking. Phone 555-416-8870 email dalemorvik@quillpost.example web www.thesaltedharvest.example, Key West fl. The color or colors should have some green and other colors that look good together that stimulate appetite and give a clean healthy image. To help with a thought process, words like food as medicine, medicine is food, good nutrition is health but at the same time I do not want a lot of medical symbols that me it look clinical. Any questions please contact me.

```html
<!DOCTYPE html>
<html lang="en">
<head>
<meta charset="utf-8">
<title>Chef Dale Morvik – Business Card</title>
<link rel="stylesheet" href="https://fonts.googleapis.com/css2?family=Josefin+Sans:wght@300;400;600&family=Nunito:wght@700&display=swap">
<style>
  :root {
    --card-white: #ffffff;
    --ink: #151515;
    --ink-soft: #3a3a3a;
    --forest: #006a38;
    --leaf: #2f8f52;
    --sage: #74ad92;
    --band-text: #f2f7f3;
  }
  html, body {
    margin: 0;
    padding: 0;
    width: 1200px;
    height: 802px;
    overflow: hidden;
    background: var(--card-white);
  }
  .card {
    position: relative;
    width: 1200px;
    height: 802px;
    background: var(--card-white);
    overflow: hidden;
    font-family: "Josefin Sans", sans-serif;
    color: var(--ink);
  }
  .card__web {
    position: absolute;
    left: 14px;
    top: 14px;
    margin: 0;
    font-family: "Nunito", sans-serif;
    font-weight: 700;
    font-size: 25px;
    letter-spacing: 2px;
    color: var(--ink);
  }
  .card__art {
    position: absolute;
    inset: 0;
    width: 1200px;
    height: 802px;
  }
  .card__identity {
    position: absolute;
    left: 60px;
    top: 302px;
  }
  .card__name {
    margin: 0;
    font-weight: 400;
    font-size: 68px;
    line-height: 1;
    letter-spacing: 1px;
    color: var(--ink);
    white-space: nowrap;
  }
  .card__tagline {
    margin: 14px 0 0 2px;
    font-weight: 400;
    font-size: 33px;
    letter-spacing: 0.5px;
    color: var(--ink-soft);
    white-space: nowrap;
  }
  .card__tagline .accent-organic { color: var(--leaf); }
  .card__tagline .accent-health { color: var(--forest); font-weight: 600; }
  .card__contact {
    position: absolute;
    top: 738px;
    margin: 0;
    font-weight: 400;
    font-size: 32px;
    line-height: 1;
    color: var(--band-text);
    white-space: nowrap;
  }
  .card__phone { left: 10px; }
  .card__email { right: 20px; }
</style>
</head>
<body>
  <main class="card">
    <p class="card__web">www.thesaltedharvest.example</p>

    <svg class="card__art" viewBox="0 0 1200 802">
      <rect class="utensil-spoon-left" role="img" aria-label="Sage green spoon silhouette entering from the left edge"
            x="0" y="256" width="250" height="206" rx="90" fill="var(--sage)"/>
      <rect class="utensil-fork-spoon" role="img" aria-label="Sage green fork and spoon silhouettes, angled, on the right"
            x="800" y="207" width="400" height="390" rx="110" fill="var(--sage)"/>
      <polygon class="zigzag-band" fill="var(--forest)"
        points="0,622 83,706 170,612 258,706 345,612 433,706 520,612 608,706 695,612 783,706 870,612 958,706 1045,612 1133,706 1200,625 1200,802 0,802"/>
    </svg>

    <div class="card__identity">
      <h1 class="card__name">CHEF DALE MORVIK</h1>
      <p class="card__tagline">Natural <span class="accent-organic">Organic</span> &amp; <span class="accent-health">Health</span> Supportive Cook</p>
    </div>

    <p class="card__contact card__phone">P: 555 416 8870</p>
    <p class="card__contact card__email">dalemorvik@quillpost.example</p>
  </main>
</body>
</html>
```